" Não vendemos nossos serviços "no varejo". Somos chamados a participar de projetos de investimento no Brasil ainda na fase de concepção, sob acordo de confidencialidade, buscando alimentar a modelagem financeira com os inputs tributários que frequentemente são cruciais na definição de viabilidade do projeto. Também somos chamados por nossos clientes para avaliar ou alocar contratualmente riscos decorrentes de contingências fiscais, especialmente em fusões e aquisições de empresas. E, ainda, patrocinar defesas ou pleitos em processos administrativos ou judiciais, sempre tendo como parte adversária o fisco (federal, estadual ou municipal). Atuamos em um ambiente profissional onde ética, compliance, qualidade e comprometimento são premissas. O propósito de nossa empresa é a criação de valor de modo sustentável, em questões fiscais, para negócios empreendidos no Brasil. "

```html
<!DOCTYPE html>
<html lang="pt-BR">
<head>
<meta charset="utf-8">
<title>Moura Lacerda Tavares Advogados — Pasta institucional</title>
<link rel="stylesheet" href="https://fonts.googleapis.com/css2?family=Roboto:wght@300;400&display=swap">
<style>
  :root {
    --backdrop: #eceef1;
    --paper: #ffffff;
    --paper-edge: #dfe2e6;
    --brand-navy: #1f3a78;
    --brand-slate: #5f6f86;
    --ghost-type: #ebedf0;
    --pocket-shade: #f6f7f9;
  }
  * { margin: 0; padding: 0; box-sizing: border-box; }
  html, body {
    width: 1200px;
    height: 1200px;
    overflow: hidden;
    background: var(--backdrop);
    font-family: "Roboto", Arial, sans-serif;
  }
  .folder-spread {
    position: absolute;
    top: 250px;
    left: 70px;
    display: flex;
    gap: 40px;
  }
  .folder-cover,
  .folder-inside {
    position: relative;
    width: 510px;
    height: 680px;
    background: var(--paper);
    border: 1px solid var(--paper-edge);
    overflow: hidden;
  }
  .folder-cover { border-top-right-radius: 34px; }
  .folder-inside { border-top-left-radius: 34px; }

  .brand-lockup {
    position: absolute;
    top: 230px;
    left: 62px;
    display: flex;
    align-items: center;
    gap: 16px;
  }
  .brand-square {
    width: 58px;
    height: 58px;
    background: var(--brand-navy);
  }
  .brand-name {
    list-style: none;
    color: var(--brand-slate);
    font-weight: 300;
    font-size: 15px;
    line-height: 16px;
    letter-spacing: 0.04em;
    text-transform: uppercase;
  }

  .cover-tab {
    position: absolute;
    bottom: 0;
    left: 50%;
    width: 260px;
    height: 18px;
    transform: translateX(-50%);
    background: var(--brand-navy);
    border-radius: 10px 10px 0 0;
  }

  .inside-pocket {
    position: absolute;
    left: 0;
    right: 0;
    bottom: 0;
    height: 360px;
    background: var(--pocket-shade);
    border-top: 1px solid var(--paper-edge);
  }
  .pocket-ghost-words {
    list-style: none;
    position: absolute;
    top: 24px;
    left: 30px;
    color: var(--ghost-type);
    font-weight: 300;
    font-size: 62px;
    line-height: 72px;
    letter-spacing: 0.02em;
    text-transform: uppercase;
  }
  .pocket-signature {
    position: absolute;
    right: 28px;
    bottom: 22px;
    color: var(--brand-navy);
    font-weight: 300;
    font-size: 13px;
    letter-spacing: 0.06em;
    text-transform: uppercase;
  }
</style>
</head>
<body>
  <main class="folder-spread">
    <section class="folder-cover" aria-label="Capa da pasta">
      <div class="brand-lockup">
        <span class="brand-square" aria-hidden="true"></span>
        <ul class="brand-name">
          <li>Moura</li>
          <li>Lacerda</li>
          <li>Tavares</li>
          <li>Advogados</li>
        </ul>
      </div>
      <span class="cover-tab" aria-hidden="true"></span>
    </section>

    <section class="folder-inside" aria-label="Interior da pasta">
      <div class="inside-pocket">
        <ul class="pocket-ghost-words" aria-hidden="true">
          <li>Moura</li>
          <li>Lacerda</li>
          <li>Tavares</li>
          <li>Advogados</li>
        </ul>
        <p class="pocket-signature">Moura Lacerda Tavares Advogados</p>
      </div>
    </section>
  </main>
</body>
</html>
```